Full page ad in a magazine

We would like an ad designed to be placed for advertising in magazines, theater playbills, etc. I have attached a copy of some previous ads that were done for us, although they need much improvement and redesigned. We have won "best chiropractor" awards that can be seen on our website home page at ferncliffspineandjoint.com

```html
<!DOCTYPE html>
<html lang="en">
<head>
<meta charset="utf-8">
<title>Ferncliff Spine &amp; Joint Center – Magazine Ad</title>
<link rel="stylesheet" href="https://fonts.googleapis.com/css2?family=Montserrat:ital,wght@0,600;0,800;1,800&family=Questrial&family=EB+Garamond:ital@1&family=Cinzel:wght@700&display=swap">
<style>
  :root {
    --brand-red: #8b1416;
    --ink: #2b2b2b;
    --panel: #434345;
    --paper: #f1f1f1;
    --white: #ffffff;
    --muted: #c9c9c9;
  }
  * { margin: 0; padding: 0; box-sizing: border-box; }
  html, body { width: 1141px; height: 1200px; overflow: hidden; background: var(--paper); }
  .ad {
    position: relative; width: 1141px; height: 1200px; overflow: hidden;
    background: linear-gradient(135deg, #f7f7f7 0%, #ececec 55%, #f4f4f4 100%);
    font-family: "Questrial", sans-serif; color: var(--ink);
  }
  .brand { position: absolute; left: 84px; top: 62px; display: flex; align-items: center; gap: 28px; }
  .brand-square { width: 206px; height: 222px; background: #9a9a9a; }
  .brand-name {
    font-family: "Cinzel", serif; font-weight: 700; color: var(--brand-red);
    font-size: 62px; line-height: 1.12; letter-spacing: 2px;
  }
  .headline {
    position: absolute; left: 76px; top: 362px;
    font-family: "Montserrat", sans-serif; font-style: italic; font-weight: 800;
    font-size: 80px; line-height: 92px; color: var(--brand-red); letter-spacing: -1px;
  }
  .services-bar {
    position: absolute; left: 76px; top: 554px; width: 660px; height: 54px;
    background: var(--panel); color: var(--white);
    font-size: 38px; line-height: 54px; padding-left: 16px;
  }
  .conditions { position: absolute; left: 76px; top: 636px; display: grid; grid-template-columns: 294px 240px; row-gap: 10px; list-style: none; }
  .conditions li { font-size: 34px; line-height: 38px; display: flex; align-items: center; gap: 12px; }
  .conditions li::before {
    content: ""; width: 20px; height: 20px; border-radius: 50%;
    background: radial-gradient(circle, var(--brand-red) 0 5px, #f1dede 5px 7px, var(--brand-red) 7px);
  }
  .insurance { position: absolute; left: 76px; top: 802px; font-family: "EB Garamond", serif; font-style: italic; font-size: 32px; color: #444; }
  .hero-photo {
    position: absolute; left: 690px; top: 322px; width: 451px; height: 621px;
    background: linear-gradient(180deg, #9a9a9a 0%, #b9b9b9 50%, #a3a3a3 100%);
  }
  .contact-panel { position: absolute; left: 0; top: 943px; width: 1141px; height: 189px; background: var(--panel); }
  .portrait {
    position: absolute; left: 56px; top: 879px; width: 232px; height: 232px; border-radius: 50%;
    background: linear-gradient(160deg, #6c6a6a, #3a3a3c 70%);
  }
  .doctor-tab {
    position: absolute; left: 268px; top: 928px; width: 294px; height: 34px;
    background: var(--brand-red); color: var(--white); font-size: 27px; line-height: 34px; padding-left: 52px;
    clip-path: polygon(8% 0, 100% 0, 98% 100%, 0 100%);
  }
  .phone { position: absolute; left: 316px; top: 982px; display: flex; align-items: center; gap: 10px; color: var(--white);
    font-family: "Montserrat", sans-serif; font-weight: 800; font-size: 42px; }
  .phone svg { width: 44px; height: 44px; }
  .address { position: absolute; left: 320px; top: 1040px; color: var(--white); font-size: 24px; line-height: 32px; font-style: normal; }
  .awards-label { position: absolute; left: 769px; top: 973px; width: 318px; display: flex; align-items: center; gap: 8px; color: var(--muted); font-size: 16px; white-space: nowrap; }
  .awards-label::before, .awards-label::after { content: ""; flex: 1; height: 1px; background: #8a8a8a; }
  .awards { position: absolute; left: 774px; top: 1008px; display: flex; gap: 11px; }
  .award-badge { width: 90px; height: 84px; background: var(--white); }
  .award-badge.blue { width: 100px; background: #3f5aa8; }
  .web-band {
    position: absolute; left: 0; top: 1132px; width: 1141px; height: 68px; background: var(--brand-red);
    color: var(--white); text-align: center; font-size: 38px; line-height: 68px;
  }
  .web-band strong { font-family: "Montserrat", sans-serif; font-weight: 600; font-size: 36px; }
</style>
</head>
<body>
<main class="ad">
  <header class="brand">
    <div class="brand-square"></div>
    <div class="brand-name">FERNCLIFF<br>SPINE &amp; JOINT<br>CENTER</div>
  </header>

  <h1 class="headline">NECK OR<br>BACK PAIN?</h1>
  <div class="services-bar">CHIROPRACTIC • MASSAGE</div>

  <ul class="conditions">
    <li>Back Pain</li><li>Joint Pain</li>
    <li>Neck Pain</li><li>Sciatica</li>
    <li>Headaches</li><li>Fatigue</li>
  </ul>
  <p class="insurance">Medicare and most Insurance accepted.</p>

  <div class="hero-photo" role="img" aria-label="Photo of a man from behind holding his neck and lower back"></div>

  <section class="contact-panel"></section>
  <div class="portrait" role="img" aria-label="Portrait photo of the chiropractor in a suit"></div>
  <div class="doctor-tab">Marcus Hale, DC</div>
  <div class="phone">
    <svg viewBox="0 0 44 44" aria-hidden="true">
      <circle cx="22" cy="22" r="21" fill="#fff"/>
      <path d="M15 11l5 6-3 3c1.5 3.5 4 6 7 7l3-3 6 5-3 4c-9 0-18-9-18-18z" fill="#8b1416"/>
    </svg>
    <span>555-218-4470</span>
  </div>
  <address class="address">2714 Linden Hall Rd., #105<br>Ferncliff, VA 23990</address>

  <div class="awards-label">Best Chiropractor</div>
  <div class="awards">
    <div class="award-badge"></div>
    <div class="award-badge blue"></div>
    <div class="award-badge blue"></div>
  </div>

  <footer class="web-band">www.<strong>ferncliffspineandjoint</strong>.com</footer>
</main>
</body>
</html>
```